New management consulting website

I need a 4-5 page website that I can manage in WordPress on Sitehaven.example for a new management consulting company. The website is www.tolvira.example and the company name is Tolvira Group LLC. The attached spec has an example of a draft site, layout and actual copy and includes company and contact information. I have more high-res images I can send.

Must include instruction/assistance loading the site to my WordPress dashboard.

Target Market(s)

Any business, especially SAAS

Industry/Entity Type

Consultant

Coding

Coded - Design and coding required

Number of Pages Required

4 page

Font styles to use
Sans Serif

Colors
0456a4

Requirements
Must have
• Modern and stylish

```html
<!DOCTYPE html>
<html lang="en">
<head>
<meta charset="utf-8">
<title>Tolvira Consulting</title>
<link rel="stylesheet" href="https://fonts.googleapis.com/css2?family=Poppins:wght@400;500;600;700&family=Raleway:wght@400;500;600;700&display=swap">
<style>
:root{
  --navy:#1d3b68;
  --navy-deep:#0c1a3b;
  --blue-band:#274a7c;
  --accent:#0456a4;
  --ink:#1a1a1a;
  --text:#444;
  --grey:#8d8d90;
  --grey-light:#e4e4e6;
  --dark:#2d2c2a;
  --white:#fff;
}
*{box-sizing:border-box;margin:0;padding:0}
html,body{width:1200px;height:3427px;overflow:hidden}
body{position:relative;background:var(--white);font-family:"Raleway",sans-serif;color:var(--text)}
.abs{position:absolute}

/* header */
.site-header{position:absolute;top:0;left:0;width:1200px;height:72px;background:var(--white)}
.brand{position:absolute;font-family:"Poppins",sans-serif;font-weight:600;color:var(--navy);letter-spacing:1px}
.site-header .brand{left:162px;top:20px;font-size:24px}
.main-nav a{position:absolute;top:27px;font-family:"Poppins",sans-serif;font-size:14px;color:#444;text-decoration:none}
.main-nav .active{color:var(--ink);border-bottom:1px solid var(--ink);padding-bottom:4px}
.btn{position:absolute;display:flex;align-items:center;justify-content:center;border-radius:22px;font-family:"Poppins",sans-serif;font-weight:500;color:var(--white);background:var(--navy);font-size:13px;text-transform:uppercase}
.btn-quote{left:934px;top:20px;width:116px;height:35px;text-transform:none;font-size:14px}

/* hero */
.hero{position:absolute;top:72px;left:0;width:1200px;height:669px}
.hero-title-light{left:149px;top:222px;font-family:"Poppins",sans-serif;font-size:58px;font-weight:400;color:var(--white);line-height:1}
.hero-title-bold{left:149px;top:292px;font-family:"Poppins",sans-serif;font-size:70px;font-weight:700;color:var(--white);line-height:1}
.hero-lead{left:149px;top:382px;width:520px;font-family:"Poppins",sans-serif;font-size:19px;line-height:28px;color:var(--white)}
.btn-apply{left:149px;top:468px;width:177px;height:44px;justify-content:flex-start;padding-left:56px;font-size:15px;text-transform:uppercase;background:var(--navy)}
.btn-apply::before{content:"";position:absolute;left:6px;top:6px;width:32px;height:32px;border-radius:50%;background:var(--white)}

/* about */
.dot{position:absolute;border-radius:50%}
.about-eyebrow{left:621px;top:825px;font-family:"Poppins",sans-serif;font-size:16px;font-weight:600;color:var(--navy)}
.about-title{left:621px;top:852px;font-family:"Poppins",sans-serif;font-size:39px;font-weight:600;color:var(--ink)}
.rule{position:absolute;height:2px}
.about-copy{left:621px;top:922px;width:430px;font-size:13.5px;line-height:27px;color:#444}
.btn-history{left:619px;top:1118px;width:166px;height:40px;font-size:13px}

/* sections */
.section-title{position:absolute;left:0;width:1200px;text-align:center;font-family:"Poppins",sans-serif;color:var(--white);text-transform:uppercase}
.section-copy{position:absolute;left:0;width:1200px;text-align:center;font-size:13.5px}
.help-card{position:absolute;top:1655px;width:278px;height:204px;border-radius:10px}
.card-tab{position:absolute;left:30px;right:30px;bottom:0;height:30px;border-radius:10px 10px 0 0;background:var(--navy-deep);color:var(--white);font-family:"Poppins",sans-serif;font-size:13px;font-weight:600;text-align:center;line-height:34px;text-transform:uppercase}
.learn-more{position:absolute;top:1872px;width:278px;text-align:center;font-family:"Poppins",sans-serif;font-size:12.5px;font-weight:500;color:#b9c3d3}
.learn-more span{border-bottom:1px solid #b9c3d3;padding-bottom:3px}

/* contact */
.contact-title{position:absolute;left:0;width:1126px;top:2632px;text-align:center;font-family:"Poppins",sans-serif;font-size:31px;font-weight:600;color:var(--navy)}
.field{position:absolute;border:1px solid #c9c9c9;background:var(--white);font-family:"Poppins",sans-serif;font-size:16px;color:#555;padding:12px 18px}
.btn-submit{left:483px;top:2920px;width:158px;height:46px;background:var(--white);border:2px solid var(--navy);color:var(--navy);font-size:15px;font-weight:600;border-radius:24px}

/* footer */
.footer-brand{left:0;width:1200px;text-align:center;top:3160px;font-size:40px;color:#3d5d92;font-weight:500}
.footer-nav a{position:absolute;top:3280px;font-family:"Poppins",sans-serif;font-size:17px;color:var(--white);text-decoration:none}
.copyright{left:173px;top:3365px;font-size:13px;color:#d7dcea}
.social{position:absolute;top:3359px;width:30px;height:30px;border-radius:50%;background:#9a9ea8}
</style>
</head>
<body>

<header class="site-header">
  <div class="brand">TOLVIRA CONSULTING</div>
  <nav class="main-nav">
    <a class="active" style="left:592px">Home</a>
    <a style="left:661px">Services</a>
    <a style="left:754px">About us</a>
    <a style="left:843px">Contact</a>
  </nav>
  <a class="btn btn-quote">Get Quote</a>
</header>

<section class="hero">
  <svg class="abs" style="left:0;top:0" width="1200" height="669" viewBox="0 0 1200 669" role="img" aria-label="Glowing blue digital globe with network lines">
    <defs>
      <radialGradient id="globeGlow" cx="0.68" cy="0.4" r="0.6">
        <stop offset="0" stop-color="#1fb4e8"/>
        <stop offset="0.35" stop-color="#0b5bc6"/>
        <stop offset="0.75" stop-color="#062a78"/>
        <stop offset="1" stop-color="#040f2e"/>
      </radialGradient>
    </defs>
    <path d="M0 0H1200V669Q600 590 0 669Z" fill="url(#globeGlow)"/>
  </svg>
  <div class="abs hero-title-light">Management</div>
  <div class="abs hero-title-bold">Consulting</div>
  <p class="abs hero-lead">Brightlane Funding Group offers a streamlined approach to commercial financing solutions.</p>
  <a class="btn btn-apply">Apply Now</a>
</section>

<section class="about">
  <div class="dot" style="left:168px;top:879px;width:25px;height:25px;background:var(--navy)"></div>
  <div class="dot" style="left:481px;top:906px;width:26px;height:26px;background:#4a4a4a"></div>
  <div class="dot" style="left:211px;top:1186px;width:25px;height:25px;background:var(--navy)"></div>
  <div class="abs" role="img" aria-label="Consultant on a video call on a laptop" style="left:243px;top:821px;width:171px;height:154px;background:linear-gradient(135deg,#5f6f80,#2c3440)"></div>
  <div class="abs" role="img" aria-label="Businessman thinking at a desk" style="left:149px;top:986px;width:169px;height:150px;background:linear-gradient(135deg,#9aa6b3,#3a4352)"></div>
  <div class="abs" role="img" aria-label="Hands reviewing charts on paper" style="left:327px;top:986px;width:232px;height:230px;background:linear-gradient(135deg,#b6bcc4,#5b6370)"></div>
  <div class="abs" style="left:304px;top:950px;width:38px;height:38px;background:var(--white);transform:rotate(45deg)"></div>

  <div class="abs about-eyebrow">ABOUT US</div>
  <h2 class="abs about-title">Tolvira Consulting</h2>
  <div class="rule" style="left:621px;top:906px;width:90px;background:var(--ink)"></div>
  <p class="abs about-copy">Lorem Ipsum is simply dummy text of the printing and typesetting industry. Lorem Ipsum has been the industry's standard dummy text ever since the 1500s, when an unknown printer took a galley of type and scrambled it to make a type specimen book. It has survived not only five centuries, but also the leap into electronic typesetting, remaining essentially unchanged.</p>
  <a class="btn btn-history">Our History</a>
</section>

<svg class="abs" style="left:0;top:1317px" width="1200" height="1254" viewBox="0 0 1200 1254">
  <polygon points="0,17 419,87 0,146" fill="var(--grey)"/>
  <polygon points="0,146 1050,0 1050,12 0,166" fill="var(--grey-light)"/>
  <polygon points="0,166 1200,0 1200,652 0,825" fill="var(--blue-band)"/>
  <defs>
    <linearGradient id="climb" x1="0" y1="0" x2="1" y2="0">
      <stop offset="0" stop-color="#3a3936"/>
      <stop offset="0.6" stop-color="#2b2a28"/>
      <stop offset="1" stop-color="#141414"/>
    </linearGradient>
  </defs>
  <polygon points="0,825 1200,652 1200,1254 0,1254" fill="url(#climb)" role="img" aria-label="Silhouette of climbers helping each other up a mountain at dusk"/>
</svg>

<section class="help">
  <h2 class="section-title" style="top:1494px;font-size:37px;font-weight:400"><b style="font-weight:700">Who do</b> we help?</h2>
  <div class="rule" style="left:563px;top:1550px;width:74px;background:var(--white)"></div>
  <p class="section-copy" style="top:1570px;color:#dfe5ef;line-height:23px">Lorem Ipsum is simply dummy text of the printing and typesetting industry.<br>Lorem Ipsum has been the industry's standard dummy text.</p>

  <div class="help-card" role="img" aria-label="Two executives meeting in an office" style="left:150px;background:linear-gradient(135deg,#a9a39a,#3b3a3a)"><div class="card-tab">Strategy &amp; Operations</div></div>
  <div class="help-card" role="img" aria-label="Team analysing printed charts with a tablet" style="left:462px;background:linear-gradient(135deg,#4b4c50,#c9a866)"><div class="card-tab">Data Analysis &amp; Insights</div></div>
  <div class="help-card" role="img" aria-label="Smiling colleagues in a business meeting" style="left:772px;background:linear-gradient(135deg,#c7ccd2,#585f6a)"><div class="card-tab">Leadership</div></div>
  <div class="learn-more" style="left:150px"><span>LEARN MORE</span> &rarr;</div>
  <div class="learn-more" style="left:462px"><span>LEARN MORE</span> &rarr;</div>
  <div class="learn-more" style="left:772px"><span>LEARN MORE</span> &rarr;</div>
</section>

<section class="amazing">
  <h2 class="section-title" style="top:2202px;font-size:37px;font-weight:600">Amazing things for you</h2>
  <div class="rule" style="left:563px;top:2261px;width:74px;background:var(--white)"></div>
  <p class="section-copy" style="left:300px;width:600px;top:2288px;font-size:15px;line-height:24px;color:#b5b5b5">Always write benefits over features. Mention all the benefits or services with some real examples. Focus on how you can help and benefit your user. Use simple words so that you don't confuse people. Say as much in as few words as possible.</p>
  <a class="btn" style="left:516px;top:2399px;width:168px;height:40px;font-size:13px">Our History</a>
</section>

<section class="contact">
  <h2 class="contact-title">GET IN TOUCH</h2>
  <div class="field" style="left:255px;top:2706px;width:296px;height:44px">Your Name</div>
  <div class="field" style="left:573px;top:2706px;width:296px;height:44px">Subject</div>
  <div class="field" style="left:255px;top:2774px;width:296px;height:44px">Email Address</div>
  <div class="field" style="left:255px;top:2842px;width:296px;height:44px">Phone</div>
  <div class="field" style="left:573px;top:2774px;width:296px;height:112px"></div>
  <a class="btn btn-submit">Submit</a>
</section>

<footer>
  <svg class="abs" style="left:0;top:2990px" width="1200" height="437" viewBox="0 0 1200 437">
    <polygon points="778,90 1200,30 1200,143" fill="var(--grey)"/>
    <polygon points="150,3 1200,148 1200,170 0,0" fill="var(--grey-light)"/>
    <polygon points="0,0 1200,170 1200,437 0,437" fill="var(--navy-deep)"/>
  </svg>
  <div class="brand abs footer-brand">TOLVIRA CONSULTING</div>
  <nav class="footer-nav">
    <a style="left:399px">Home</a>
    <a style="left:503px">About us</a>
    <a style="left:629px">Services</a>
    <a style="left:757px">Contact</a>
  </nav>
  <p class="abs copyright">&copy; 2021 Tolvira Consulting. All Rights Reserved.</p>
  <span class="social" style="left:891px"></span>
  <span class="social" style="left:927px"></span>
  <span class="social" style="left:963px"></span>
  <span class="social" style="left:1000px"></span>
</footer>

</body>
</html>
```